Crestfield Row sign

24"x36" sign for new home construction job site. Located in affluent in-town neighborhood in Midwest. Traditional american style homes. 2nd generation construction company. Sign needs to convey strength and elegance but not overly elaborate. Competition most has signs consisting of text.

Sign text reads:
Crestfield Row Builders
Custom Luxury for Over 20 years
248-391-0827

Target Market(s)

Upper middle income home buyers

Industry/Entity Type

Construction

Font styles to use
Serif
Decorative

Requirements
Must have
• Logo image no more than 2 colors
Nice to have
• Should be visible and legible from distance of 30'
Should not have
• Not just image of house as logo

```html
<!DOCTYPE html>
<html lang="en">
<head>
<meta charset="utf-8">
<title>Crestfield Row Builders — Job Site Sign</title>
<link rel="stylesheet" href="https://fonts.googleapis.com/css2?family=Open+Sans:wght@400;600;700&display=swap">
<style>
  :root {
    --sign-orange: #f38836;
    --sign-charcoal: #363435;
    --sign-silver: #9d9d9d;
    --sign-white: #ffffff;
    --rule-grey: #a9a9a9;
  }
  html, body {
    margin: 0;
    padding: 0;
    width: 1200px;
    height: 800px;
    overflow: hidden;
    background: var(--sign-orange);
  }
  .sign {
    position: relative;
    width: 1200px;
    height: 800px;
    font-family: "Open Sans", Arial, sans-serif;
    color: var(--sign-white);
  }
  .sign__backdrop {
    position: absolute;
    inset: 0;
  }
  .brand-mark {
    position: absolute;
    left: 548px;
    top: 84px;
    width: 104px;
    height: 104px;
    background: var(--sign-orange);
  }
  .brand-name {
    position: absolute;
    left: 0;
    width: 1200px;
    text-align: center;
    margin: 0;
    font-weight: 600;
    color: var(--sign-white);
  }
  .brand-name__primary {
    top: 262px;
    font-size: 86px;
    line-height: 1;
    letter-spacing: -1px;
  }
  .brand-rule {
    position: absolute;
    left: 202px;
    top: 368px;
    width: 796px;
    height: 1px;
    background: var(--rule-grey);
  }
  .brand-name__secondary {
    top: 388px;
    font-size: 50px;
    line-height: 1;
    letter-spacing: 46px;
    padding-left: 46px;
  }
  .tagline {
    position: absolute;
    left: 0;
    top: 558px;
    width: 1200px;
    margin: 0;
    text-align: center;
    font-size: 50px;
    font-weight: 400;
    line-height: 1;
  }
  .contact {
    position: absolute;
    left: 120px;
    top: 634px;
    display: flex;
    align-items: center;
    gap: 60px;
  }
  .contact__icon {
    width: 62px;
    height: 76px;
    flex: none;
  }
  .contact__phone {
    font-size: 118px;
    font-weight: 400;
    line-height: 1;
    letter-spacing: 1px;
  }
</style>
</head>
<body>
  <main class="sign">
    <svg class="sign__backdrop" width="1200" height="800" viewBox="0 0 1200 800" aria-hidden="true">
      <rect width="1200" height="800" fill="var(--sign-orange)"/>
      <path class="panel-dark" d="M22 22 H1178 V532 C1110 492 1030 466 920 468 C720 474 420 532 22 548 Z" fill="var(--sign-charcoal)"/>
      <path class="swoosh" d="M22 503 C300 526 700 486 1090 480 C720 476 330 528 22 520 Z" fill="var(--sign-silver)"/>
      <rect class="frame-line" x="19" y="19" width="1162" height="762" fill="none" stroke="var(--sign-white)" stroke-width="2"/>
    </svg>

    <div class="brand-mark" aria-hidden="true"></div>
    <h1 class="brand-name brand-name__primary">CRESTFIELD ROW</h1>
    <div class="brand-rule" aria-hidden="true"></div>
    <p class="brand-name brand-name__secondary">BUILDERS</p>

    <p class="tagline">Custom Luxury for Over 20 years</p>

    <div class="contact">
      <svg class="contact__icon" viewBox="0 0 62 76" aria-hidden="true">
        <rect x="4" y="4" width="54" height="68" rx="6" fill="none" stroke="var(--sign-white)" stroke-width="5"/>
        <rect x="17" y="20" width="28" height="30" fill="none" stroke="var(--sign-white)" stroke-width="5"/>
        <line x1="25" y1="62" x2="37" y2="62" stroke="var(--sign-white)" stroke-width="4"/>
      </svg>
      <span class="contact__phone">248-391-0827</span>
    </div>
  </main>
</body>
</html>
```